New business card for Building services company

I own a small 1 person business which primarily works at heights. I gain access to my work areas via ladders and use safety harnesses. I conduct gutter cleaning, roof cleaning with a pressure cleaner(water blaster), ground level pressure cleaning (driveways, footpaths and walls), I also do small handy-man jobs & gardening/ tree trimming.

I have just had a logo designed by Sketch Harbor, which I will upload. I'd like to see the themes followed through.
I like the colour of aqua or the colours what is in the logo.

I live in tropical north Queensland in Cairns, Australia. It is where the rain forest meets the Verdant Shoal Reef. On average it is 30+ degrees C.
Updates

Hello all designers. Thankyou for all the submissions so far. The following are my business details which I need on the card-

PELIKOR Roof, Gutter & Pressure Cleaning Services.
Director -Dylan Morwick
Ph 0417 552 803
Email- roofcleaning@vexlonet.com.au
ABN -38 924 417 205

Please include the following services which my business conducts-
*Gutter Cleaning
*Pressure Cleaning- Roof's, Driveways etc
*Minor Roof, Gutter & Building Maintenance
*Garden waste removal & complex cleanups

Public Liability upto $10 Million
Working at Heights Cert.

Quote-                                     Date-

Hi everyone,  could you please ensure you have -"Quote" and "Date" on the card. I'll need space to hand write details on the card for the specific details.        

Requirements
Must have
• The logo attached must be included.
• The rear side of the card is dedicated to job quoted and price of the job.
• *Please include- Quote price, Quote date. etc
• Including the tasks I do at work around the side of the card- Gutter Cleaning; Roof Cleaning, Gutter Maintenance; Gardening; Pressure Cleaning Roof's, Driveways etc.
Nice to have
• The rear side to have a ladder

```html
<!DOCTYPE html>
<html lang="en">
<head>
<meta charset="utf-8">
<title>PELIKOR Business Card</title>
<link rel="stylesheet" href="https://fonts.googleapis.com/css2?family=Cinzel:wght@500;700&family=Sorts+Mill+Goudy&family=Tinos:wght@700&display=swap">
<style>
  :root {
    --page: #eceeed;
    --teal: #0aa495;
    --teal-soft: #8fd9d1;
    --teal-mist: #d2f1ee;
    --white: #ffffff;
    --navy: #353a8a;
    --green: #1c7a58;
  }
  * { box-sizing: border-box; margin: 0; padding: 0; }
  html, body {
    width: 1034px; height: 1200px; overflow: hidden;
    background: var(--page);
  }
  .card {
    position: absolute;
    width: 751px; height: 446px;
    background: linear-gradient(to bottom,
      var(--teal) 0%, var(--teal-soft) 12%, var(--white) 21%,
      var(--white) 66%, var(--teal-mist) 73%, var(--teal-soft) 84%, var(--teal) 100%);
    color: var(--navy);
    overflow: hidden;
  }
  .card--front { left: 140px; top: 99px; }
  .card--back  { left: 142px; top: 628px; }

  .centered { position: absolute; left: 0; right: 0; text-align: center; }

  .brand-name {
    top: 44px;
    font-family: "Cinzel", serif; font-weight: 700;
    font-size: 108px; line-height: 1; letter-spacing: 2px;
    color: var(--navy);
  }
  .brand-tagline {
    top: 186px;
    font-family: "Cinzel", serif; font-weight: 700;
    font-size: 19.5px; letter-spacing: 0.2px;
  }
  .call-line {
    top: 222px;
    font-family: "Cinzel", serif; font-weight: 700;
    font-size: 46px; line-height: 1;
    color: var(--green);
  }
  .contact-name {
    top: 296px;
    font-family: "Sorts Mill Goudy", serif; font-size: 29px;
  }
  .contact-role {
    top: 332px;
    font-family: "Sorts Mill Goudy", serif; font-size: 22px;
  }
  .contact-email {
    top: 364px;
    font-family: "Sorts Mill Goudy", serif; font-size: 23px; font-weight: 700;
    letter-spacing: 0.3px;
  }

  .back-text { font-family: "Tinos", serif; font-weight: 700; position: absolute; }
  .field { top: 55px; font-size: 19px; }
  .field--quote { left: 49px; }
  .field--date  { left: 341px; }

  .services { position: absolute; left: 48px; top: 148px; list-style: none; }
  .services li {
    font-family: "Tinos", serif; font-weight: 700;
    font-size: 17.5px; height: 33.6px; letter-spacing: 0.2px;
    display: flex; align-items: flex-start;
  }
  .services li::before {
    content: ""; width: 8px; height: 8px; margin: 6px 11px 0 0;
    background: linear-gradient(to bottom, var(--navy), var(--teal));
    flex: none;
  }
  .abn { left: 49px; top: 378px; font-size: 20px; font-weight: 400; font-family: "Tinos", serif; }
  .abn { font-weight: 700; }

  .worker-art {
    position: absolute; left: 488px; top: 64px; width: 263px; height: 382px;
    background: linear-gradient(to bottom, rgba(53,58,138,0.55), rgba(53,58,138,0.85));
    clip-path: polygon(45% 0, 62% 0, 66% 40%, 100% 78%, 100% 100%, 0 100%, 0 88%, 36% 45%);
  }
</style>
</head>
<body>
  <section class="card card--front" aria-label="Business card front">
    <h1 class="centered brand-name">PELIKOR</h1>
    <p class="centered brand-tagline">ROOF, GUTTER &amp; PRESSURE CLEANING SERVICES</p>
    <p class="centered call-line">CALL&nbsp; 0417 552 803</p>
    <p class="centered contact-name">Dylan Morwick</p>
    <p class="centered contact-role">Director</p>
    <p class="centered contact-email">roofcleaning@vexlonet.com.au</p>
  </section>

  <section class="card card--back" aria-label="Business card back">
    <p class="back-text field field--quote">Quote -</p>
    <p class="back-text field field--date">Date -</p>
    <ul class="services">
      <li>GUTTER CLEANING</li>
      <li>PRESSURE CLEANING- ROOF'S, DRIVEWAYS ETC</li>
      <li>MINOR ROOF, GUTTER &amp; BUILDING MAINTENANCE</li>
      <li>GARDEN WASTE REMOVAL &amp; COMPLEX CLEANUPS</li>
      <li>PUBLIC LIABILITY UPTO $10 MILLION</li>
      <li>WORKING AT HEIGHTS CERT</li>
    </ul>
    <p class="back-text abn">ABN 38 924 417 205</p>
    <div class="worker-art" role="img" aria-label="Silhouette of a worker pressure cleaning a roof ridge above a ladder"></div>
  </section>
</body>
</html>
```